Do an outer bag for a popular chocolate product

Mellow Pip is a small chocolate wafer, we have had a lot of demmand for the product to be packed in a bag to be bought in bulk. The bag will be 150 g and will contain about 13 small bars. The dimensions of bag flat are 240 mm long by 260mm wide. The bag should be modelled on the design of the chocolate bar attached. It should have a very similar look to the actual product and have a clear window in the centre of the pack through which the product is visible

Target Market(s)

Middle income consumers of chocoalate in Zimbabwe buying for family sharing, gifting or parties

Industry/Entity Type

Product

Requirements
Must have
• A window in the centre of the pack where the product is visible. The outer bag must be similar to the chocolate design as attached in the photo
Nice to have
• The use of half tones and swirls.

```html
<!DOCTYPE html>
<html lang="en">
<head>
<meta charset="utf-8">
<title>Mellow Pip – Choc Coated Wafer Bag</title>
<link rel="stylesheet" href="https://fonts.googleapis.com/css2?family=Figtree:wght@700;800&family=Cinzel:wght@500&family=Arimo:wght@400&display=swap">
<style>
  :root {
    --canvas: #ececec;
    --bag-dark: #2e0a0b;
    --bag-maroon: #5a1418;
    --bag-red: #8e1e2a;
    --bag-crimson: #a42433;
    --gold: #f2b51a;
    --gold-deep: #d99a0c;
    --cream: #f6efe6;
    --white: #ffffff;
    --wafer: #c98a55;
    --choc: #6a3720;
  }
  html, body {
    margin: 0;
    width: 1200px;
    height: 1200px;
    overflow: hidden;
    background: var(--canvas);
  }
  .canvas {
    position: relative;
    width: 1200px;
    height: 1200px;
  }
  .bag {
    position: absolute;
    left: 283px;
    top: 230px;
    width: 632px;
    height: 738px;
    overflow: hidden;
  }
  .bag-art {
    position: absolute;
    inset: 0;
  }
  .bag-gloss {
    position: absolute;
    inset: 0;
    pointer-events: none;
  }
  .brand-name {
    position: absolute;
    top: 80px;
    left: 0;
    width: 100%;
    text-align: center;
    font-family: "Figtree", sans-serif;
    font-weight: 700;
    font-size: 34px;
    color: var(--white);
    letter-spacing: 1px;
  }
  .product-title {
    position: absolute;
    top: 152px;
    left: 0;
    width: 100%;
    margin: 0;
    text-align: center;
    font-family: "Figtree", sans-serif;
    font-weight: 800;
    font-size: 80px;
    line-height: 1;
    color: var(--gold);
    letter-spacing: -1px;
  }
  .product-subtitle {
    position: absolute;
    top: 244px;
    left: 0;
    width: 100%;
    text-align: center;
    font-family: "Cinzel", serif;
    font-weight: 500;
    font-size: 28px;
    color: var(--cream);
    letter-spacing: 1px;
  }
  .bar-count {
    position: absolute;
    top: 694px;
    left: 0;
    width: 100%;
    text-align: center;
    font-family: "Arimo", sans-serif;
    font-size: 18px;
    color: var(--white);
  }
</style>
</head>
<body>
<main class="canvas">
  <section class="bag">
    <svg class="bag-art" width="632" height="738" viewBox="0 0 632 738">
      <defs>
        <linearGradient id="bagBody" x1="0" y1="0" x2="0" y2="1">
          <stop offset="0" stop-color="#3a0d0f"/>
          <stop offset="0.3" stop-color="var(--bag-maroon)"/>
          <stop offset="0.5" stop-color="var(--bag-red)"/>
          <stop offset="1" stop-color="var(--bag-dark)"/>
        </linearGradient>
        <linearGradient id="swirlBand" x1="0" y1="0" x2="1" y2="0">
          <stop offset="0" stop-color="var(--bag-crimson)"/>
          <stop offset="0.5" stop-color="#7e1a24"/>
          <stop offset="1" stop-color="var(--bag-red)"/>
        </linearGradient>
        <linearGradient id="productFill" x1="0" y1="0" x2="1" y2="1">
          <stop offset="0" stop-color="var(--wafer)"/>
          <stop offset="1" stop-color="var(--choc)"/>
        </linearGradient>
        <linearGradient id="wrapperFill" x1="0" y1="0" x2="1" y2="0">
          <stop offset="0" stop-color="#4a1212"/>
          <stop offset="1" stop-color="#8a2a1e"/>
        </linearGradient>
        <linearGradient id="windowContents" x1="0" y1="0" x2="1" y2="1">
          <stop offset="0" stop-color="#9a3322"/>
          <stop offset="0.5" stop-color="#7a2418"/>
          <stop offset="1" stop-color="#5a1812"/>
        </linearGradient>
        <linearGradient id="windowSheen" x1="0" y1="0" x2="0" y2="1">
          <stop offset="0" stop-color="#ffffff" stop-opacity="0.38"/>
          <stop offset="0.18" stop-color="#ffffff" stop-opacity="0.08"/>
          <stop offset="0.8" stop-color="#ffffff" stop-opacity="0"/>
          <stop offset="1" stop-color="#ffffff" stop-opacity="0.12"/>
        </linearGradient>
        <linearGradient id="sideShade" x1="0" y1="0" x2="1" y2="0">
          <stop offset="0" stop-color="#000" stop-opacity="0.55"/>
          <stop offset="0.1" stop-color="#000" stop-opacity="0.1"/>
          <stop offset="0.5" stop-color="#000" stop-opacity="0"/>
          <stop offset="0.9" stop-color="#000" stop-opacity="0.12"/>
          <stop offset="1" stop-color="#000" stop-opacity="0.6"/>
        </linearGradient>
        <linearGradient id="topSeal" x1="0" y1="0" x2="0" y2="1">
          <stop offset="0" stop-color="#1c0506"/>
          <stop offset="0.6" stop-color="#3c0e10"/>
          <stop offset="1" stop-color="#3c0e10" stop-opacity="0"/>
        </linearGradient>
        <linearGradient id="bottomSeal" x1="0" y1="0" x2="0" y2="1">
          <stop offset="0" stop-color="#000" stop-opacity="0"/>
          <stop offset="1" stop-color="#000" stop-opacity="0.55"/>
        </linearGradient>
        <linearGradient id="highlight" x1="0" y1="0" x2="1" y2="0">
          <stop offset="0" stop-color="#fff" stop-opacity="0"/>
          <stop offset="0.5" stop-color="#fff" stop-opacity="0.22"/>
          <stop offset="1" stop-color="#fff" stop-opacity="0"/>
        </linearGradient>
      </defs>

      <rect class="bag-body" width="632" height="738" fill="url(#bagBody)"/>

      <path class="swirl-band" d="M0 290 C160 250 420 300 632 270 L632 420 C470 450 300 450 0 470 Z" fill="url(#swirlBand)" opacity="0.85"/>
      <path class="swirl-lower" d="M0 470 C260 440 480 470 632 400 L632 738 L0 738 Z" fill="var(--bag-dark)"/>
      <path class="swirl-gold-line" d="M0 462 C250 430 470 460 632 392" fill="none" stroke="var(--gold)" stroke-width="4"/>
      <path class="swirl-gold-line-fine" d="M0 474 C250 444 470 474 632 406" fill="none" stroke="var(--gold-deep)" stroke-width="1.5"/>

      <rect class="wrapped-bars" x="18" y="318" width="282" height="150" rx="10" fill="url(#wrapperFill)" role="img" aria-label="Two wrapped Mellow Pip wafer bars"/>
      <rect class="product-shot" x="322" y="292" width="286" height="172" rx="14" fill="url(#productFill)" role="img" aria-label="Chocolate coated wafer bar, one piece cut to show the wafer layers"/>

      <g class="clear-window">
        <rect x="102" y="482" width="460" height="183" rx="14" fill="url(#windowContents)" role="img" aria-label="Wrapped wafer bars seen through the clear window"/>
        <rect class="window-film" x="102" y="482" width="460" height="183" rx="14" fill="url(#windowSheen)"/>
        <path class="window-glint" d="M150 482 L215 482 L140 665 L75 665 Z" fill="#ffffff" opacity="0.08" transform="translate(40 0)"/>
        <path class="window-glint-thin" d="M300 482 L318 482 L243 665 L225 665 Z" fill="#ffffff" opacity="0.1"/>
        <path class="window-glint-right" d="M470 482 L520 482 L460 665 L410 665 Z" fill="#ffffff" opacity="0.06"/>
        <rect class="window-edge" x="103" y="483" width="458" height="181" rx="13" fill="none" stroke="#ffffff" stroke-opacity="0.35" stroke-width="2"/>
        <rect class="window-rim" x="100" y="480" width="464" height="187" rx="16" fill="none" stroke="#000000" stroke-opacity="0.35" stroke-width="2"/>
      </g>
    </svg>

    <svg class="bag-gloss" width="632" height="738" viewBox="0 0 632 738" aria-hidden="true">
      <rect class="top-seal" x="0" y="0" width="632" height="34" fill="url(#topSeal)"/>
      <path class="top-seal-line" d="M0 30 C200 22 430 22 632 30" fill="none" stroke="#ffffff" stroke-opacity="0.12" stroke-width="2"/>
      <path class="upper-sheen" d="M40 40 C220 28 420 28 600 40 L600 62 C420 50 220 50 40 62 Z" fill="url(#highlight)"/>
      <rect class="side-shade" width="632" height="738" fill="url(#sideShade)"/>
      <path class="right-pillow-highlight" d="M600 40 C618 200 618 520 600 700 L610 700 C628 520 628 200 610 40 Z" fill="#ffffff" opacity="0.1"/>
      <path class="left-pillow-highlight" d="M22 60 C10 220 10 520 22 690 L30 690 C18 520 18 220 30 60 Z" fill="#ffffff" opacity="0.06"/>
      <path class="lower-sheen" d="M20 680 C220 664 420 664 612 680 L612 690 C420 676 220 676 20 690 Z" fill="url(#highlight)"/>
      <rect class="bottom-seal" x="0" y="700" width="632" height="38" fill="url(#bottomSeal)"/>
    </svg>

    <div class="brand-name">Harlow</div>
    <h1 class="product-title">Mellow Pip</h1>
    <div class="product-subtitle">Choc Coated Wafer</div>
    <div class="bar-count">Contains 13 Bars</div>
  </section>
</main>
</body>
</html>
```